Very personalised Wedding Invitation

I want a wedding invitation very unique and personalised with the menus, ceremony time table and thank you cards. I want a mix of a nice traditional style with indian style touch. I don't want a colourful invitation, it can have max. two different colours.

The bride's name is Rosalind and the groom's name is Tarun

Reason: None of the designs submitted are what I am looking for

Target Market(s)

Invitations, personalised invitations,

Industry/Entity Type

Wedding

Logo Text

Our initials T&R To use in our wedding things

Font styles to use
Decorative
Script

Requirements
Must have
Nice to have
• I would like a chic design with a bit of indian style
Should not have

```html
<!DOCTYPE html>
<html lang="en">
<head>
<meta charset="utf-8">
<title>Rosalind &amp; Tarun – Wedding Invitation</title>
<link rel="stylesheet" href="https://fonts.googleapis.com/css2?family=Dancing+Script:wght@500;600&family=Open+Sans:wght@400;700&display=swap">
<style>
  :root {
    --backdrop: #d9d6d2;
    --paper: #e9d8bf;
    --paper-shade: #dcc9ae;
    --rose-light: #c77b8f;
    --rose-deep: #a9536e;
    --lace: #fbf6ee;
  }
  * { margin: 0; padding: 0; box-sizing: border-box; }
  html, body {
    width: 1200px; height: 1134px; overflow: hidden;
    background: var(--backdrop);
  }
  .spread {
    position: absolute; left: 40px; top: 287px;
    width: 1120px; height: 560px;
    display: flex;
    box-shadow: 0 6px 18px rgba(0,0,0,0.18);
  }
  .panel {
    position: relative; width: 560px; height: 560px;
    background: var(--paper); overflow: hidden;
  }
  .panel--back {
    background: linear-gradient(90deg, var(--paper) 80%, var(--paper-shade) 100%);
  }
  .panel--front {
    background: linear-gradient(90deg, var(--paper-shade) 0%, var(--paper) 6%);
  }
  .back-ornament {
    position: absolute; left: 218px; top: 219px;
    width: 124px; height: 124px; border-radius: 50%;
    background: radial-gradient(circle, rgba(251,246,238,0.9) 0%, rgba(251,246,238,0.55) 60%, rgba(251,246,238,0) 72%);
  }
  .lace-ornament {
    position: absolute; left: 86px; top: -200px;
    width: 400px; height: 400px; border-radius: 50%;
    background: radial-gradient(circle, rgba(251,246,238,0.85) 0%, rgba(251,246,238,0.6) 70%, rgba(251,246,238,0) 76%);
  }
  .names {
    position: absolute; left: 0; top: 0; width: 100%;
    font-family: "Dancing Script", cursive; font-weight: 500;
    white-space: nowrap;
  }
  .names__bride {
    position: absolute; left: 84px; top: 212px;
    font-size: 66px; line-height: 1; color: var(--rose-light);
  }
  .names__amp {
    position: absolute; left: 322px; top: 234px;
    font-size: 62px; line-height: 1; color: var(--rose-deep);
  }
  .names__groom {
    position: absolute; left: 196px; top: 294px;
    font-size: 72px; line-height: 1; color: var(--rose-deep);
  }
  .divider {
    position: absolute; left: 245px; top: 392px; width: 72px; height: 14px;
  }
  .details {
    position: absolute; left: 0; top: 432px; width: 100%;
    text-align: center; font-family: "Open Sans", sans-serif; color: var(--rose-deep);
  }
  .details__date {
    font-weight: 700; font-size: 17px; letter-spacing: 2.5px; line-height: 20px;
  }
  .details__place {
    margin-top: 12px;
    font-weight: 700; font-size: 18px; letter-spacing: 2.5px; line-height: 20px;
  }
  .details__note {
    margin-top: 8px;
    font-weight: 400; font-size: 12.5px; letter-spacing: 1.5px; line-height: 16px;
  }
</style>
</head>
<body>
  <main class="spread">
    <section class="panel panel--back">
      <div class="back-ornament" role="img" aria-label="Small white Indian mandala motif"></div>
    </section>
    <section class="panel panel--front">
      <div class="lace-ornament" role="img" aria-label="White lace mandala ornament at the top edge"></div>
      <h1 class="names">
        <span class="names__bride">Rosalind</span>
        <span class="names__amp">&amp;</span>
        <span class="names__groom">Tarun</span>
      </h1>
      <svg class="divider" viewBox="0 0 72 14" aria-hidden="true">
        <path d="M2 8 C 18 2, 30 2, 38 7 S 58 12, 70 5" fill="none" stroke="var(--lace)" stroke-width="3" stroke-linecap="round"/>
      </svg>
      <div class="details">
        <p class="details__date">8TH OF JULY 2018</p>
        <p class="details__place">BROOKFIELD, NY 10512</p>
        <p class="details__note">DINNER AND DANCING TO FOLLOW</p>
      </div>
    </section>
  </main>
</body>
</html>
```